Medical Company in need of Modern business card design for new Wound Care clinic.

Modern business card design for our Woundcare company. Logo and description of services can be found on our website; https://www.tovrel-woundcare.com/

```html
<!DOCTYPE html>
<html lang="en">
<head>
<meta charset="UTF-8">
<title>Tovrel Woundcare – Business Card</title>
<link rel="stylesheet" href="https://fonts.googleapis.com/css2?family=Poppins:wght@400;500;600&family=Roboto:wght@400&display=swap">
<style>
  :root {
    --backdrop: #1d1d1e;
    --card-white: #ffffff;
    --ink: #2a2a2a;
    --ink-soft: #6b6b6b;
    --gold: #b8862b;
    --gold-light: #d9a441;
    --black: #0e0e0e;
    --divider: #9a9a9a;
  }
  * { box-sizing: border-box; margin: 0; padding: 0; }
  html, body {
    width: 1200px;
    height: 900px;
    overflow: hidden;
    background: var(--backdrop);
  }
  .canvas {
    width: 1200px;
    height: 900px;
    display: flex;
    flex-direction: column;
    align-items: center;
    justify-content: center;
    gap: 40px;
  }
  .card {
    width: 700px;
    height: 400px;
    position: relative;
    overflow: hidden;
    box-shadow: 0 18px 40px rgba(0,0,0,0.55);
  }
  /* Front */
  .card-front { background: var(--card-white); }
  .brand {
    position: absolute;
    left: 62px;
    top: 176px;
    display: flex;
    align-items: center;
    gap: 14px;
  }
  .brand-square {
    width: 22px;
    height: 22px;
    background: var(--gold);
  }
  .brand-name {
    font-family: "Poppins", sans-serif;
    font-weight: 400;
    font-size: 21px;
    letter-spacing: 4px;
    color: var(--ink);
  }
  .divider {
    position: absolute;
    left: 404px;
    top: 92px;
    width: 1px;
    height: 176px;
    background: var(--divider);
  }
  .details {
    position: absolute;
    left: 424px;
    top: 92px;
    width: 260px;
  }
  .person-name {
    font-family: "Poppins", sans-serif;
    font-weight: 500;
    font-size: 20px;
    color: var(--ink);
    letter-spacing: 0.5px;
  }
  .person-title {
    font-family: "Roboto", sans-serif;
    font-size: 14px;
    color: var(--gold);
    margin-top: 1px;
  }
  .address {
    font-family: "Roboto", sans-serif;
    font-size: 13px;
    line-height: 18px;
    color: var(--ink-soft);
    margin-top: 14px;
  }
  .contact-list {
    list-style: none;
    margin-top: 10px;
  }
  .contact-list li {
    display: flex;
    align-items: center;
    gap: 7px;
    font-family: "Roboto", sans-serif;
    font-size: 13px;
    line-height: 19px;
    color: var(--ink-soft);
  }
  .contact-icon { width: 12px; height: 12px; flex: none; }
  .base-band {
    position: absolute;
    left: 0;
    bottom: 0;
    width: 100%;
    height: 18px;
    display: flex;
  }
  .base-band-dark { width: 404px; background: var(--black); }
  .base-band-gold { flex: 1; background: linear-gradient(90deg, var(--gold), var(--gold-light) 60%, var(--gold)); }
  /* Back */
  .card-back {
    background: radial-gradient(ellipse at 30% 60%, #2e2e30 0%, #141415 70%);
  }
</style>
</head>
<body>
<main class="canvas">
  <section class="card card-front" aria-label="Business card front">
    <div class="brand">
      <span class="brand-square"></span>
      <span class="brand-name">TOVREL WOUNDCARE</span>
    </div>
    <div class="divider"></div>
    <div class="details">
      <p class="person-name">DORIAN KESSEL</p>
      <p class="person-title">Founder &amp; CEO</p>
      <p class="address">2180 Marlow Ave Ste 210 PMB<br>418220 Dallas, TX 75239</p>
      <ul class="contact-list">
        <li>
          <svg class="contact-icon" viewBox="0 0 24 24" fill="var(--gold)"><path d="M6.6 10.8a15.1 15.1 0 0 0 6.6 6.6l2.2-2.2a1 1 0 0 1 1-.25 11.4 11.4 0 0 0 3.6.57 1 1 0 0 1 1 1V20a1 1 0 0 1-1 1A17 17 0 0 1 3 4a1 1 0 0 1 1-1h3.5a1 1 0 0 1 1 1c0 1.25.2 2.45.57 3.57a1 1 0 0 1-.25 1z"/></svg>
          972-555-0147
        </li>
        <li>
          <svg class="contact-icon" viewBox="0 0 24 24" fill="none" stroke="var(--gold)" stroke-width="2.4"><rect x="2" y="5" width="20" height="14"/><path d="M2 5l10 8 10-8"/></svg>
          info@tovrel-woundcare.com
        </li>
        <li>
          <svg class="contact-icon" viewBox="0 0 24 24" fill="none" stroke="var(--gold)" stroke-width="2"><circle cx="12" cy="12" r="10"/><ellipse cx="12" cy="12" rx="4.5" ry="10"/><path d="M2 12h20M4 7h16M4 17h16"/></svg>
          www.tovrel-woundcare.com
        </li>
      </ul>
    </div>
    <div class="base-band">
      <span class="base-band-dark"></span>
      <span class="base-band-gold"></span>
    </div>
  </section>

  <section class="card card-back" role="img" aria-label="Card back: black stock covered with a repeated brand-mark pattern in gloss black and silver foil, with one mark in gold foil"></section>
</main>
</body>
</html>
```